Music Web page

We are the largest community of artists, bands, podcasters and creators of music. We need web pages design.

What we need:
1. Registration form page
- Full Name
- Username
- Email Address
- Password
- Captcha

2. Songs/Artists gallery page
- Cover
- Simple MP3 Player
- Share | Like | Comments

3. Contact us page
- Name
- Email
- Phone
- Message
- Captcha

Send me a registration form first, If it makes me "hands on the air" , then I will continue to work with you.

Artists

Colors
eb1f27

Requirements
Nice to have
• Dark / black color for background

```html
<!DOCTYPE html>
<html lang="en">
<head>
<meta charset="utf-8">
<title>Music Web Page – Register</title>
<link rel="stylesheet" href="https://fonts.googleapis.com/css2?family=Bebas+Neue&family=Oswald:wght@400;500&family=Questrial&family=Arimo:wght@400;700&display=swap">
<style>
  :root {
    --red: #eb1f27;
    --red-bright: #ff0022;
    --page-bg: #1b1b1b;
    --bar-top: #2c2c2c;
    --bar-bottom: #111111;
    --panel: #000000;
    --panel-soft: #161616;
    --field: #2b2b2b;
    --white: #ffffff;
    --ink: #111111;
    --muted: #bbbbbb;
  }
  * { box-sizing: border-box; margin: 0; padding: 0; }
  html, body { width: 926px; height: 1200px; overflow: hidden; }
  body {
    position: relative;
    background: repeating-linear-gradient(45deg, #1d1d1d 0 2px, #191919 2px 4px);
    font-family: "Arimo", Arial, sans-serif;
    color: var(--white);
  }

  /* Header */
  .site-header {
    position: absolute; left: 0; top: 0; width: 926px; height: 55px;
    background: linear-gradient(var(--bar-top), var(--bar-bottom));
    border-bottom: 1px solid #000;
  }
  .brand {
    position: absolute; left: 115px; top: 12px;
    font-family: "Bebas Neue", sans-serif; font-size: 30px; letter-spacing: 1px;
    color: var(--white); line-height: 32px;
  }
  .main-nav { position: absolute; left: 326px; top: 0; display: flex; height: 55px; }
  .main-nav a {
    display: block; height: 55px; line-height: 55px; padding: 0 20px;
    font-family: "Oswald", sans-serif; font-size: 17px; color: var(--white);
    text-decoration: none; border-left: 1px solid #000; border-right: 1px solid #3a3a3a;
  }
  .main-nav a.is-active { background: linear-gradient(#3c3c3c, #262626); width: 74px; text-align: center; padding: 0; }
  .search {
    position: absolute; left: 630px; top: 16px; width: 181px; height: 22px;
    background: var(--white); border: 1px solid #999;
    font-size: 12px; color: #aaa; padding: 3px 6px;
  }
  .search svg { position: absolute; right: 5px; top: 3px; }

  /* Main frame */
  .main {
    position: absolute; left: 92px; top: 55px; width: 743px; height: 1063px;
    background: var(--panel); box-shadow: 0 0 14px #000;
  }

  /* Hero */
  .hero {
    position: absolute; left: 0; top: 0; width: 743px; height: 461px;
    background: radial-gradient(ellipse at 52% 8%, #f3e3b6 0%, #c49a58 22%, #5a4128 50%, #1c140e 78%, #0a0807 100%);
  }
  .hero-title {
    position: absolute; left: 28px; top: 29px;
    font-family: "Questrial", sans-serif; font-weight: 700; font-size: 31px; color: #222;
  }
  .hero-lead {
    position: absolute; left: 28px; top: 63px; width: 270px;
    font-family: "Questrial", sans-serif; font-size: 19px; line-height: 23px; color: #1a1a1a;
  }

  /* Registration form */
  .register { position: absolute; left: 488px; top: 33px; width: 231px; }
  .register-head {
    height: 40px; text-align: center;
    background: linear-gradient(90deg, rgba(90,80,60,.85), rgba(150,130,95,.85));
  }
  .register-head h2 { font-size: 20px; font-weight: 700; line-height: 24px; padding-top: 2px; }
  .register-head p { font-size: 8px; font-weight: 700; }
  .field {
    height: 41px; margin-top: 14px; background: var(--field);
    color: #ddd; font-size: 12px; text-align: center; line-height: 41px;
  }
  .register-head + .field { margin-top: 15px; }
  .captcha { display: flex; height: 41px; margin-top: 13px; background: var(--field); }
  .captcha-code {
    width: 91px; background: var(--red-bright); color: var(--white);
    font-family: "Questrial", sans-serif; font-size: 16px; line-height: 41px; text-align: center;
  }
  .captcha-tools { display: flex; gap: 5px; margin-top: 4px; }
  .submit {
    margin-top: 29px; height: 41px; background: var(--red-bright);
    font-size: 15px; text-align: center; line-height: 41px;
  }
  .form-links { display: flex; justify-content: space-between; margin-top: 6px; font-size: 8px; font-weight: 700; }
  .form-links a { color: var(--red-bright); text-decoration: underline; }

  /* Promo */
  .promo-photo {
    position: absolute; left: 24px; top: 498px; width: 327px; height: 195px;
    border: 2px solid #ddd;
    background: linear-gradient(120deg, #6f6a4e, #4a4a36 45%, #2c2a22 70%, #8a7c63);
  }
  .promo-title { position: absolute; left: 372px; top: 496px; font-size: 22px; color: var(--red-bright); font-weight: 400; }
  .promo-text {
    position: absolute; left: 374px; top: 530px; width: 345px;
    font-size: 15px; line-height: 18.4px; text-align: justify;
  }
  .btn-more {
    position: absolute; left: 374px; top: 612px; width: 140px; height: 42px;
    background: var(--red-bright); font-size: 15px; line-height: 42px; text-align: center;
  }

  /* Latest */
  .latest { position: absolute; left: 24px; top: 715px; width: 695px; height: 321px; background: var(--panel-soft); }
  .latest-title { position: absolute; left: 36px; top: 12px; font-family: "Bebas Neue", sans-serif; font-size: 24px; color: var(--red-bright); font-weight: 400; }
  .latest-title a { font-family: "Arimo", sans-serif; font-size: 11px; color: var(--white); margin-left: 8px; font-weight: 700; }
  .track { position: absolute; top: 52px; width: 185px; height: 234px; }
  .track-cover { height: 134px; }
  .track-text {
    height: 66px; overflow: hidden; background: var(--white); color: var(--ink);
    font-size: 9px; line-height: 12px; padding: 7px 7px 0 8px;
  }
  .track-stats {
    height: 34px; background: var(--red-bright); display: flex; align-items: center;
    justify-content: space-between; padding: 0 13px; font-size: 10px; color: #900;
  }
  .track-stats span { display: flex; align-items: center; gap: 3px; }

  /* Footer */
  .social { position: absolute; left: 378px; top: 1138px; display: flex; gap: 7px; }
  .social span { width: 27px; height: 27px; background: #555; }
  .copyright { position: absolute; left: 0; top: 1177px; width: 926px; text-align: center; font-size: 7px; font-weight: 700; }
</style>
</head>
<body>
  <header class="site-header">
    <div class="brand">JUMPSTAGE</div>
    <nav class="main-nav">
      <a href="#" class="is-active">HOME</a>
      <a href="#">GALLERY</a>
      <a href="#">CONTACT US</a>
    </nav>
    <div class="search">Search
      <svg width="13" height="13" viewBox="0 0 13 13"><circle cx="5.5" cy="5.5" r="4" fill="none" stroke="#222" stroke-width="1.8"/><line x1="8.5" y1="8.5" x2="12" y2="12" stroke="#222" stroke-width="2"/></svg>
    </div>
  </header>

  <main class="main">
    <section class="hero" role="img" aria-label="Concert crowd with raised hands under warm stage lights">
      <h1 class="hero-title">Hear and Jump around</h1>
      <p class="hero-lead">Aliquam tristique vestibulum<br>Aenean sit amet justo id<br>nibh sollicitudin lacinia.</p>

      <form class="register">
        <div class="register-head">
          <h2>REGISTER NOW!</h2>
          <p>or login with your email</p>
        </div>
        <div class="field">FULLNAME</div>
        <div class="field">USERNAME</div>
        <div class="field">EMAIL &nbsp;ADDRESS</div>
        <div class="field">PASSWORD</div>
        <div class="captcha"><div class="captcha-code">X2189AS</div></div>
        <div class="captcha-tools">
          <svg width="11" height="11" viewBox="0 0 12 12"><path d="M10 6a4 4 0 1 1-1.2-2.8" fill="none" stroke="#ff0022" stroke-width="1.6"/><path d="M9 0v4H5z" fill="#ff0022"/></svg>
          <svg width="13" height="11" viewBox="0 0 13 11"><path d="M0 4h3l4-3v9L3 7H0z" fill="#ff0022"/><path d="M9 3q2 2.5 0 5M10.5 1.5q3.5 4 0 8" fill="none" stroke="#ff0022" stroke-width="1.2"/></svg>
        </div>
        <div class="submit">SUBMIT</div>
        <div class="form-links"><a>LOGIN</a><a>RESET</a></div>
      </form>
    </section>

    <div class="promo-photo" role="img" aria-label="Musician seated outdoors playing an acoustic guitar"></div>
    <h2 class="promo-title">Do you create music &amp; audio?</h2>
    <p class="promo-text">Lorem ipsum dolor sit amet, consectetur adipiscing elit. Phasellus sed cursus est, laoreet porttitor orci. Quisque sollicitudin consectetur ante, in venenatis purus adipiscing porttitor.</p>
    <div class="btn-more">FIND OUT MORE</div>

    <section class="latest">
      <h2 class="latest-title">LATEST MUSICS<a href="#">View all</a></h2>

      <article class="track" style="left:39px">
        <div class="track-cover" role="img" aria-label="Portrait cover of a female singer" style="background:linear-gradient(135deg,#e8e2d8,#9c8878 60%,#3b2c24)"></div>
        <p class="track-text">Morbi faucibus velit id mauris consec-<br>tetur pretium. Nullam id eleifend mi.<br>Praesent auctor arcu massa, id pellen-<br>tesque nisi egestas sed.</p>
        <div class="track-stats">
          <span><svg width="14" height="12" viewBox="0 0 14 12"><path d="M2 9l4-4M6 3l2-2a2.5 2.5 0 0 1 3.5 3.5l-2 2M8 9l-2 2A2.5 2.5 0 0 1 2.5 7.5l2-2" fill="none" stroke="#900" stroke-width="2"/></svg>80</span>
          <span><svg width="13" height="12" viewBox="0 0 13 12"><path d="M0 5h3v7H0zM4 5l3-5c2 0 2 1.5 1.5 4H12l-1 8H4z" fill="#900"/></svg>320</span>
          <span><svg width="13" height="12" viewBox="0 0 13 12"><path d="M0 0h13v8H5l-3 4V8H0z" fill="#900"/></svg>28</span>
        </div>
      </article>

      <article class="track" style="left:250px">
        <div class="track-cover" role="img" aria-label="Portrait cover of a female artist" style="background:linear-gradient(135deg,#6b2a3a,#a05a52 50%,#2a1418)"></div>
        <p class="track-text">Morbi faucibus velit id mauris consec-<br>tetur pretium. Nullam id eleifend mi.<br>Praesent auctor arcu massa, id pellen-<br>tesque nisi egestas sed.</p>
        <div class="track-stats">
          <span><svg width="14" height="12" viewBox="0 0 14 12"><path d="M2 9l4-4M6 3l2-2a2.5 2.5 0 0 1 3.5 3.5l-2 2M8 9l-2 2A2.5 2.5 0 0 1 2.5 7.5l2-2" fill="none" stroke="#900" stroke-width="2"/></svg>80</span>
          <span><svg width="13" height="12" viewBox="0 0 13 12"><path d="M0 5h3v7H0zM4 5l3-5c2 0 2 1.5 1.5 4H12l-1 8H4z" fill="#900"/></svg>320</span>
          <span><svg width="13" height="12" viewBox="0 0 13 12"><path d="M0 0h13v8H5l-3 4V8H0z" fill="#900"/></svg>28</span>
        </div>
      </article>

      <article class="track" style="left:461px">
        <div class="track-cover" role="img" aria-label="Country guitarist performing on stage" style="background:linear-gradient(135deg,#1e3a5c,#5c7a96 45%,#8a6a48 70%,#2a2218)"></div>
        <p class="track-text">Morbi faucibus velit id mauris consec-<br>tetur pretium. Nullam id eleifend mi.<br>Praesent auctor arcu massa, id pellen-<br>tesque nisi egestas sed.</p>
        <div class="track-stats">
          <span><svg width="14" height="12" viewBox="0 0 14 12"><path d="M2 9l4-4M6 3l2-2a2.5 2.5 0 0 1 3.5 3.5l-2 2M8 9l-2 2A2.5 2.5 0 0 1 2.5 7.5l2-2" fill="none" stroke="#900" stroke-width="2"/></svg>80</span>
          <span><svg width="13" height="12" viewBox="0 0 13 12"><path d="M0 5h3v7H0zM4 5l3-5c2 0 2 1.5 1.5 4H12l-1 8H4z" fill="#900"/></svg>320</span>
          <span><svg width="13" height="12" viewBox="0 0 13 12"><path d="M0 0h13v8H5l-3 4V8H0z" fill="#900"/></svg>28</span>
        </div>
      </article>
    </section>
  </main>

  <footer>
    <div class="social" aria-label="Social links">
      <span></span><span></span><span></span><span></span><span></span>
    </div>
    <p class="copyright">© 2014 MUSIC WEB PAGE</p>
  </footer>
</body>
</html>
```